KTR Engineering Business Card Design

We’re looking for an elegant, clean, and timeless business card design that communicates experience, capability, and reliability.

KTR Engineering was established in 1995 , we are a Government Contracting company providing Professional Services to the Ministry of Harbor Works, Frontier Stewardship and the Waypoint Consortium. Our capabilities include: Acquisition & Program Management; Intelligence & Security Operations; Cyber, IT & Network Operations; Lifecycle Logistics & Asset Readiness; C5ISR Systems Engineering & Sustainment.

We want the card to reflect a straightforward, confident approach to business. The design should feel polished and professional without being flashy or overly corporate.

Design Direction
Clean, sophisticated, and uncluttered
Elegant but understated
Strong typography and thoughtful spacing
A timeless aesthetic rather than something overly trendy
Confident and established, with a sense of substance
Easy to read and practical in a real-world business setting

The overall impression should be: “These are experienced professionals who know what they’re doing, do what they say, and can be relied upon.”

We’re open to creative interpretations. The finished card should feel distinctive through its typography, proportions, layout, and attention to detail rather than through excessive graphics or visual effects.

We’re looking for a design that would make a potential client immediately feel that they’re dealing with a capable, trustworthy, and established company.

Company Colors: Navy and Gold/Yellow (but you do not need to use these colors on the card)
Company Name: KTR Engineering Associates, Inc. (known as KTR Engineering)
Website: ktrengineering.example
Company Logo: Navy & Gold (other variations attached)

```html
<!DOCTYPE html>
<html lang="en">
<head>
<meta charset="utf-8">
<title>KTR Engineering Business Card</title>
<link href="https://fonts.googleapis.com/css2?family=Arimo:wght@400;700&display=swap" rel="stylesheet">
<style>
  :root {
    --backdrop: #171717;
    --navy: #1f2a5e;
    --ink: #ffffff;
    --ink-soft: #eef0f6;
  }
  * { margin: 0; padding: 0; box-sizing: border-box; }
  html, body {
    width: 1200px;
    height: 1059px;
    overflow: hidden;
    background: var(--backdrop);
    font-family: "Arimo", Arial, sans-serif;
    color: var(--ink);
  }
  .card {
    position: absolute;
    background: var(--navy);
    border-radius: 18px;
  }
  .card--front { left: 257px; top: 90px; width: 687px; height: 389px; }
  .card--back  { left: 254px; top: 547px; width: 693px; height: 393px; }

  .wordmark {
    position: absolute;
    left: 0; right: 0;
    text-align: center;
    font-weight: 700;
    color: var(--ink);
    line-height: 1;
    letter-spacing: 1px;
  }
  .card--front .wordmark { top: 88px; font-size: 78px; }
  .card--back .wordmark  { top: 172px; font-size: 102px; }

  .identity {
    position: absolute;
    right: calc(687px - 316px);
    top: 258px;
    text-align: right;
    white-space: nowrap;
  }
  .identity__name {
    font-weight: 700;
    font-size: 22px;
    line-height: 26px;
  }
  .identity__role {
    font-size: 17px;
    line-height: 24px;
    color: var(--ink-soft);
  }
  .divider {
    position: absolute;
    left: 343px;
    top: 243px;
    width: 1px;
    height: 79px;
    background: var(--ink-soft);
  }
  .contacts {
    position: absolute;
    left: 368px;
    top: 238px;
    list-style: none;
  }
  .contacts li {
    display: flex;
    align-items: center;
    height: 31px;
    font-size: 17px;
    white-space: nowrap;
  }
  .contacts svg {
    width: 13px;
    height: 13px;
    margin-right: 9px;
    fill: var(--ink);
    flex: none;
  }
</style>
</head>
<body>
  <section class="card card--front">
    <div class="wordmark">KTR</div>
    <div class="identity">
      <div class="identity__name">Maren L. Ashdown</div>
      <div class="identity__role">Principal Engineer</div>
    </div>
    <div class="divider"></div>
    <ul class="contacts">
      <li>
        <svg viewBox="0 0 24 24" aria-hidden="true"><path d="M6.6 10.8a15.1 15.1 0 0 0 6.6 6.6l2.2-2.2a1 1 0 0 1 1-.25 11.4 11.4 0 0 0 3.6.57 1 1 0 0 1 1 1V20a1 1 0 0 1-1 1A17 17 0 0 1 3 4a1 1 0 0 1 1-1h3.5a1 1 0 0 1 1 1c0 1.25.2 2.45.57 3.6a1 1 0 0 1-.25 1z"/></svg>
        (555) 014-2290
      </li>
      <li>
        <svg viewBox="0 0 24 24" aria-hidden="true"><path d="M2 9l10-6 10 6v11H2zM4 10v8h16v-8l-8 5z"/></svg>
        m.a@ktrengineering.example
      </li>
      <li>
        <svg viewBox="0 0 24 24" aria-hidden="true"><path d="M12 2a10 10 0 1 0 0 20 10 10 0 0 0 0-20zm-1 17.9A8 8 0 0 1 4.1 11H7c.3 1 1.4 1.6 1.4 2.8 0 1.4 2.6 1.5 2.6 3.2zm6.9-2.5c-.3-.8-1-1.4-1.9-1.4h-1v-3a1 1 0 0 0-1-1H8v-2h2a1 1 0 0 0 1-1V7h2a2 2 0 0 0 2-2v-.4a8 8 0 0 1 2.9 12.8z"/></svg>
        ktrengineering.example
      </li>
    </ul>
  </section>

  <section class="card card--back">
    <div class="wordmark">KTR</div>
  </section>
</body>
</html>
```